Dental Practice Website design

Design a new website for Brindle Dental Practice.
Design should be warm, neutral in colour, with some small amount of bright colour if needed but kept to a minimum. Website should look professional, high end. Home page should be easy to navigate and simple for patients to be able to book online.
Logo in files along with some examples of websites that we like. Please ask if any further info needed.
Menu should have:
About
New Patients
Treatments
Fees
Contact Us

Industry/Entity Type

Dentistry

Number of Pages Required

4 page

Font styles to use
Sans Serif

Colors

Designer to choose colors to be used in the design.

Requirements
Must have
• zorvex reviews badge, book online button,
Nice to have
• neutral, relaxing colours
Should not have
• harsh, bright colours!

```html
<!DOCTYPE html>
<html lang="en">
<head>
<meta charset="utf-8">
<title>Brindle Dental Practice – Home</title>
<link rel="stylesheet" href="https://fonts.googleapis.com/css2?family=Heebo:wght@100;200;300;400;500;700&family=Montserrat:wght@300;400;500&family=Roboto:wght@400;500;700&display=swap">
<style>
:root{
  --backdrop:#2f4548;
  --ink-dark:#17272c;
  --ink-dark-2:#1c2d32;
  --rust:#b94a2b;
  --tan:#c9a06a;
  --tan-light:#e8b988;
  --gold-head:#cf8a1c;
  --cream:#f6efdd;
  --text:#555a5c;
  --white:#ffffff;
  --band:#7a1f16;
  --accent-red:#ff3b1a;
}
*{box-sizing:border-box;margin:0;padding:0}
html,body{width:1200px;height:1200px;overflow:hidden;background:var(--backdrop)}
body{position:relative;font-family:'Roboto',sans-serif}
.page{position:absolute;left:385px;top:45px;width:690px;height:1790px;transform:scale(0.621);transform-origin:0 0;background:var(--white);overflow:hidden}
.abs{position:absolute}
.topbar{left:0;top:0;width:690px;height:84px;background:var(--ink-dark)}
.follow{left:75px;top:34px;color:var(--white);font:400 11px 'Montserrat',sans-serif;display:flex;align-items:center;gap:8px}
.social{display:flex;gap:7px;align-items:center}
.social span{font:500 8px 'Montserrat',sans-serif;color:var(--white);display:flex;align-items:center;gap:2px}
.social span::before{content:"";width:5px;height:5px;border-radius:50%;background:var(--white)}
.brand{text-align:center;color:#cfd6d8;font-family:'Heebo',sans-serif;line-height:1}
.brand .name{font-weight:200;font-size:21px;letter-spacing:1px}
.brand .sub{font-weight:300;font-size:9px;letter-spacing:.5px;margin-top:2px}
.phone{left:427px;top:35px;color:var(--white);font:400 11px 'Montserrat',sans-serif;display:flex;align-items:center;gap:8px}
.btn-outline{border:1px solid #e5e5e5;color:var(--white);font:400 10px 'Montserrat',sans-serif;display:flex;align-items:center;justify-content:center}
.hero{left:0;top:84px;width:690px;height:356px;background:linear-gradient(180deg,#767f83 0%,#6f7b80 45%,#5d6d78 100%)}
.nav{left:80px;top:99px;width:529px;height:42px;border-radius:21px;background:rgba(215,220,222,.6);display:flex;align-items:center;padding-left:11px;font:400 13px 'Roboto',sans-serif;color:#1c2226}
.nav a{text-decoration:none;color:inherit;height:34px;display:flex;align-items:center;padding:0 17px}
.nav a.active{background:var(--tan);color:var(--white);border-radius:17px;width:90px;justify-content:center;padding:0}
.hero-title{left:0;width:695px;text-align:center;color:var(--white);font-family:'Heebo',sans-serif;line-height:1}
.hero-title.main{top:168px;font-weight:100;font-size:80px;letter-spacing:2px}
.hero-title.sub{top:246px;font-weight:200;font-size:28px;letter-spacing:1px}
.btn{font:400 11px 'Montserrat',sans-serif;display:flex;align-items:center;justify-content:center;color:var(--white)}
.btn-tan{background:var(--tan)}
.btn-soft{background:var(--tan-light);box-shadow:3px 3px 4px rgba(0,0,0,.25);font-size:9px}
.panel{top:410px;height:78px;color:var(--white)}
.panel-join{left:72px;width:182px;background:var(--rust);padding:10px 12px}
.panel-join h4{font:400 9px 'Montserrat',sans-serif;margin-bottom:2px}
.panel-join p{font:400 4.6px/5.4px 'Roboto',sans-serif}
.panel-join .mini{margin-top:3px;display:inline-block;border:1px solid #f0d0c5;font:400 4.5px 'Roboto',sans-serif;padding:2px 4px}
.panel-rating{left:254px;width:181px;background:var(--ink-dark-2);padding:14px 17px;display:flex;gap:8px}
.panel-rating .badge-name{font:500 9px 'Montserrat',sans-serif;color:var(--white);align-self:center;display:flex;align-items:center;gap:3px}
.panel-rating .badge-name::before{content:"";width:6px;height:6px;border-radius:50%;background:var(--tan)}
.score{font:400 15px 'Montserrat',sans-serif}
.score small{font-size:7px;display:block;color:#c9c9c9;margin-top:3px}
.panel-hours{left:435px;width:183px;background:var(--ink-dark);padding:9px 16px;font:400 8px/15.5px 'Montserrat',sans-serif}
.panel-hours b{font-weight:500;font-size:8.5px}
.img-fill{display:block}
.heading{font:500 17px 'Roboto',sans-serif;color:var(--gold-head)}
.body-text{font:400 8.9px/14.5px 'Roboto',sans-serif;color:var(--text)}
.body-text p+p{margin-top:8px}
.welcome-title{left:304px;top:515px;width:320px;font:500 11.5px/18px 'Roboto',sans-serif;color:#2a2d2f}
.welcome-title span{font-size:16px;color:var(--gold-head);font-weight:400}
.team{left:0;top:1213px;width:690px;height:275px;background:var(--cream)}
.band{left:0;top:1488px;width:690px;height:73px;background:radial-gradient(circle at 30% 40%,#8a2a1c 0%,var(--band) 60%,#6a1a12 100%)}
.band-text{left:0;width:696px;text-align:center;color:var(--white);font:400 9px/15px 'Roboto',sans-serif}
.band-text .hl{color:var(--accent-red)}
.footer{left:0;top:1561px;width:690px;height:229px;background:var(--ink-dark)}
.footer-rule{left:0;top:1655px;width:690px;height:1px;background:#3f5257}
.footer-text{left:0;width:690px;top:1692px;text-align:center;color:#9aa3a6;font:400 9px/15px 'Roboto',sans-serif}
</style>
</head>
<body>
<main class="page">

  <header class="abs topbar"></header>
  <div class="abs follow">Follo Us
    <div class="social"><span>Quorrel</span><span>Minklet</span><span>Torvash</span><span>Bransk</span></div>
  </div>
  <div class="abs brand" style="left:285px;top:34px;width:120px">
    <div class="name">BRINDLE</div><div class="sub">DENTAL PRACTICE</div>
  </div>
  <div class="abs phone">
    <svg width="12" height="12" viewBox="0 0 24 24" fill="none" stroke="#fff" stroke-width="1.6"><path d="M5 3h4l2 5-2.5 1.5a11 11 0 0 0 6 6L16 13l5 2v4a2 2 0 0 1-2 2A17 17 0 0 1 3 5a2 2 0 0 1 2-2z"/></svg>
    00-000-00
  </div>
  <a class="abs btn-outline" style="left:515px;top:29px;width:103px;height:26px">Book Online</a>

  <section class="abs hero" role="img" aria-label="Photo of three smiling young women leaning together, dimmed with a blue-grey tint"></section>
  <nav class="abs nav">
    <a class="active">About</a><a>New Patients</a><a style="padding-left:28px">Treatments</a><a style="padding-left:24px">Fees</a><a style="padding-left:12px">Contact Us</a>
  </nav>
  <h1 class="abs hero-title main">BRINDLE</h1>
  <div class="abs hero-title sub">DENTAL PRACTICE</div>
  <a class="abs btn btn-tan" style="left:236px;top:290px;width:103px;height:31px">Book Now</a>
  <a class="abs btn-outline" style="left:351px;top:290px;width:104px;height:31px;font-size:11px;border-width:1.5px">Learn More</a>

  <div class="abs panel panel-join">
    <h4>Join Our Practice</h4>
    <p>Looking for a caring dental home? Our skilled team is ready to help, offering gentle, modern treatment for every patient in a calm and friendly setting, with flexible hours.</p>
    <span class="mini">Learn More</span>
  </div>
  <div class="abs panel panel-rating">
    <span class="badge-name">zorvex</span>
    <div class="score">5.0 <span style="color:#f5a623;font-size:12px">★★★★★</span><small>574 Reviws</small></div>
  </div>
  <div class="abs panel panel-hours">
    <b>Open Hours</b><br>Monday - Thursday 8.00 - 17.00<br>Friday9.00 - 18.00<br>Saturday9.30 - 17.30
  </div>

  <div class="abs" style="left:203px;top:511px;width:84px;height:115px;background:var(--rust)"></div>
  <div class="abs" style="left:84px;top:755px;width:134px;height:69px;background:var(--ink-dark)"></div>
  <div class="abs" style="left:95px;top:740px;width:153px;height:74px;background:var(--rust)"></div>
  <div class="abs img-fill" style="left:73px;top:518px;width:206px;height:237px;background:linear-gradient(160deg,#e6eef3,#c9d8e2 60%,#9fb7c6)" role="img" aria-label="Photo of a bright modern dental treatment room"></div>
  <div class="abs img-fill" style="left:104px;top:677px;width:192px;height:127px;background:linear-gradient(120deg,#7a4e3a,#d9d4cf 45%,#f1efec)" role="img" aria-label="Photo of a clean white reception area with wooden panels"></div>
  <h2 class="abs welcome-title"><span>Welcome to</span> our friendly dental practice nestled in the heart of beautiful Hollowmere, UK.</h2>
  <div class="abs body-text" style="left:305px;top:566px;width:315px">
    <p>Our team of dedicated dentists, hygienists and support staff are here to provide you with exceptional dental care. With a wide array of services, including general and cosmetic dentistry, orthodontics and emergency care, we're confident that we can deliver the highest quality treatment to you and your loved ones.</p>
    <p>At our practice, we believe that a visit to the dentist should be a comfortable and positive experience. We strive to create a warm and welcoming atmosphere where our patients can feel at ease and confident in the care they receive. Our state-of-the-art facilities and equipment mean that you can trust us to deliver the latest techniques and treatments to ensure your oral health is at its best.</p>
    <p>We are passionate about improving dental health and helping you achieve your brightest smile and are honoured that you're considering us for your dental needs. Please don't hesitate to contact us if you have any questions or to schedule an appointment. We look forward to welcoming you to our practice.</p>
  </div>
  <a class="abs btn btn-soft" style="left:306px;top:816px;width:120px;height:29px">Book a Consultation</a>

  <h2 class="abs heading" style="left:73px;top:874px">Join Our Practice</h2>
  <div class="abs body-text" style="left:73px;top:899px;width:245px">
    <p>If you're looking for an exceptional dental practice, we're here to help! Our team is made up of highly skilled professionals who are dedicated to ensuring that all our patients receive top-notch care in a welcoming and comfortable environment.</p>
    <p style="margin-top:14px">Whether you need a routine examination or a more specialised treatment, we have all the resources to provide you with the best dental care possible. Our practice is always up-to-date with the latest techniques and technologies to make sure that our patients receive the best possible results.</p>
    <p style="margin-top:14px">We understand that dental care can be expensive which is why we offer affordable prices to ensure that everyone has access to quality care. If you'd like to learn more about our practice, please don't hesitate to contact us.</p>
  </div>
  <a class="abs btn btn-soft" style="left:73px;top:1151px;width:119px;height:29px">See Our Practice</a>
  <div class="abs" style="left:464px;top:1045px;width:165px;height:106px;background:var(--rust)"></div>
  <div class="abs img-fill" style="left:330px;top:878px;width:289px;height:266px;background:linear-gradient(150deg,#9ba6ad,#c6cdd1 50%,#8d9aa3)" role="img" aria-label="Video still of a patient in a dental chair seen from above"></div>
  <svg class="abs" style="left:441px;top:953px" width="68" height="68" viewBox="0 0 68 68">
    <circle cx="34" cy="34" r="32" fill="none" stroke="#f0a020" stroke-width="1.5"/>
    <circle cx="34" cy="34" r="24" fill="#f0a020"/>
    <path d="M28 22 L46 34 L28 46 Z" fill="#fff"/>
  </svg>
  <div class="abs brand" style="left:330px;top:1022px;width:289px;color:#fff">
    <div class="name" style="font-size:34px;font-weight:100">BRINDLE</div>
    <div class="sub" style="font-size:11px;font-weight:200;color:#e7e7e7">DENTAL PRACTICE</div>
  </div>

  <section class="abs team"></section>
  <div class="abs img-fill" style="left:73px;top:1226px;width:226px;height:175px;background:linear-gradient(90deg,#e9eef2,#d7e1e8 50%,#c3d1db)" role="img" aria-label="Photo of two dentists in masks and white coats"></div>
  <div class="abs img-fill" style="left:73px;top:1407px;width:106px;height:71px;background:linear-gradient(135deg,#9cc7d8,#e7eef1)" role="img" aria-label="Photo of a dental team treating a patient"></div>
  <div class="abs img-fill" style="left:187px;top:1407px;width:110px;height:71px;background:linear-gradient(90deg,#5f8a4a,#c8d8c0 60%,#eef2f1)" role="img" aria-label="Photo of a receptionist at the front desk"></div>
  <h2 class="abs heading" style="left:325px;top:1224px">Our Team</h2>
  <div class="abs body-text" style="left:325px;top:1253px;width:295px;line-height:15px">
    <p>We are delighted to introduce you to our experienced and compassionate dental team. Our team comprises highly skilled dental professionals who are dedicated to providing you with high-quality dental care services. Led by our experienced dentist, each member of our team brings their own unique set of skills and expertise.</p>
    <p style="margin-top:15px">From our friendly reception staff to our knowledgeable hygienists and assistants, our team is here to ensure that you receive personalised dental care that meets your unique needs and preferences. We take great pride in providing a safe, comfortable, and welcoming environment for our patients, and we look forward to serving you with the utmost care and attention.</p>
  </div>
  <a class="abs btn btn-soft" style="left:325px;top:1443px;width:119px;height:31px">View Our Team</a>

  <section class="abs band" role="img" aria-label="Dark red band with a faint dental pattern"></section>
  <p class="abs band-text" style="top:1499px">You can call our front desk at <span class="hl">123-456-789</span> Mon - Fri 9am - 8pm, email us at<br>support@brindledental.com or fill the <span class="hl">Contact Form</span></p>
  <a class="abs btn btn-tan" style="left:305px;top:1532px;width:87px;height:22px;font:500 6px 'Roboto',sans-serif;box-shadow:2px 2px 3px rgba(0,0,0,.3)">Book Online Now</a>

  <footer class="abs footer"></footer>
  <div class="abs brand" style="left:285px;top:1604px;width:120px">
    <div class="name">BRINDLE</div><div class="sub">DENTAL PRACTICE</div>
  </div>
  <div class="abs footer-rule"></div>
  <p class="abs footer-text">Lorem ipsum dolor sit amet, consectetuer adipiscing elit, sed diam nonummy nibh euis-<br>mod tincidunt ut laoreet</p>
  <div class="abs social" style="left:0;width:690px;top:1738px;justify-content:center;gap:10px">
    <span>Quorrel</span><span>Minklet</span><span>Torvash</span><span>Bransk</span>
  </div>
</main>
</body>
</html>
```